Packaging design for handmade soap

We are looking for a packaging design for a brand new product line: handmade soaps, called VARNEO

We are looking for a design of an outer box together with the logo. We need the design for a 90x65x30mm box (see attached). We trying to get a high-end product preferable with vintage elements (but we don't want a shiny box, it will be finished with matte lacque, however logo or other certain elements could be shiny).

The design should reflect the fact that we have a handmade, all natural soap.

I uploaded a couple of packaging examples I like.

UPDATE 1: It also should have a title, which describes the product more accurate, like "Natural Soap with Seabuckthorn and Olive oil"

UPDATE 2: I would remove the expression "high-end" from the description if high end would mean a lot of flowers in the background. I would like if you would insist about the ideea of "natural" in your works

UPDATE 3: Prefered colors green and brown (which brings the ideea of nature, natural)

Target Market(s)

Women 20-45 years with above average income

Industry/Entity Type

Cosmetics

Font styles to use
Serif

Colors
9bcb3c
acd036
cadf82
f78f20
ffc214
f37122
fbed22
fece3e
faa54b

Requirements
Must have
• A literal representation of the brand VARNEO (we don't have a logo for it)

```html
<!DOCTYPE html>
<html lang="en">
<head>
<meta charset="utf-8">
<title>VARNEO Natural Handmade Soap – Box Fronts</title>
<link href="https://fonts.googleapis.com/css2?family=Quicksand:wght@500;600;700&display=swap" rel="stylesheet">
<style>
  :root {
    --page-bg: #e9ebea;
    --kraft: #cdb088;
    --kraft-dark: #c2a57c;
    --olive-line: #1f9a3e;
    --olive-band: #55b559;
    --olive-tint: #a9be8a;
    --camomile-line: #e2253c;
    --camomile-band: #ef6a6a;
    --camomile-tint: #dca88e;
    --label-white: #f8f8f6;
  }
  * { margin: 0; padding: 0; box-sizing: border-box; }
  html, body { width: 826px; height: 1200px; overflow: hidden; background: var(--page-bg); }
  body { position: relative; font-family: "Quicksand", sans-serif; }
  .box-front { position: absolute; display: block; }
  .box-front--olive { left: 52px; top: 44px; width: 722px; height: 540px; }
  .box-front--camomile { left: 54px; top: 614px; width: 728px; height: 546px; }
  .brand-name { font-family: "Quicksand", sans-serif; font-weight: 600; font-size: 80px; letter-spacing: 2px; }
  .tagline { font-family: "Quicksand", sans-serif; font-weight: 600; font-size: 23px; }
  .variant-name { font-family: "Quicksand", sans-serif; font-weight: 700; font-size: 62px; fill: #fff; }
  .variant-benefit { font-family: "Quicksand", sans-serif; font-weight: 500; font-size: 26px; fill: #fff; }
</style>
</head>
<body>

<svg class="box-front box-front--olive" viewBox="0 0 722 540" xmlns="http://www.w3.org/2000/svg">
  <defs>
    <radialGradient id="olive-backdrop" cx="50%" cy="50%" r="72%">
      <stop offset="0%" stop-color="var(--kraft)"/>
      <stop offset="70%" stop-color="var(--kraft-dark)"/>
      <stop offset="100%" stop-color="var(--olive-tint)"/>
    </radialGradient>
    <path id="label-shape" d="M120,60 Q295,-10 470,60 Q490,110 540,110 L540,150 Q590,150 590,225 Q590,300 540,300 L540,340 Q490,340 470,390 Q295,460 120,390 Q100,340 50,340 L50,300 Q0,300 0,225 Q0,150 50,150 L50,110 Q100,110 120,60 Z"/>
    <clipPath id="olive-label-clip"><use href="#label-shape"/></clipPath>
  </defs>
  <rect width="722" height="540" fill="url(#olive-backdrop)" role="img" aria-label="Line drawing of olive branches with olives on kraft paper"/>
  <g class="label" transform="translate(60 62) scale(1.037 0.987)">
    <use href="#label-shape" fill="var(--label-white)"/>
    <rect y="233" width="590" height="240" fill="var(--olive-band)" clip-path="url(#olive-label-clip)"/>
    <use href="#label-shape" fill="none" stroke="var(--olive-line)" stroke-width="10"/>
    <use href="#label-shape" fill="none" stroke="var(--olive-line)" stroke-width="2" stroke-dasharray="1 5" stroke-linecap="round" transform="translate(295 225) scale(0.93) translate(-295 -225)"/>
  </g>
  <g class="label-text" fill="var(--olive-line)">
    <text class="brand-name" x="366" y="228" text-anchor="middle">VARNEO</text>
    <text class="tagline" x="366" y="260" text-anchor="middle">Natural Handmade Soap</text>
    <text class="variant-name" x="366" y="364" text-anchor="middle">olive oil</text>
    <text class="variant-benefit" x="366" y="402" text-anchor="middle">Superior Moisturizing</text>
  </g>
</svg>

<svg class="box-front box-front--camomile" viewBox="0 0 728 546" xmlns="http://www.w3.org/2000/svg">
  <defs>
    <radialGradient id="camomile-backdrop" cx="50%" cy="50%" r="72%">
      <stop offset="0%" stop-color="var(--kraft)"/>
      <stop offset="70%" stop-color="var(--kraft-dark)"/>
      <stop offset="100%" stop-color="var(--camomile-tint)"/>
    </radialGradient>
    <clipPath id="camomile-label-clip"><use href="#label-shape"/></clipPath>
  </defs>
  <rect width="728" height="546" fill="url(#camomile-backdrop)" role="img" aria-label="Line drawing of camomile flowers on kraft paper"/>
  <g class="label" transform="translate(74 56) scale(1.027 1.027)">
    <use href="#label-shape" fill="var(--label-white)"/>
    <rect y="234" width="590" height="240" fill="var(--camomile-band)" clip-path="url(#camomile-label-clip)"/>
    <use href="#label-shape" fill="none" stroke="var(--camomile-line)" stroke-width="10"/>
    <use href="#label-shape" fill="none" stroke="var(--camomile-line)" stroke-width="2" stroke-dasharray="1 5" stroke-linecap="round" transform="translate(295 225) scale(0.93) translate(-295 -225)"/>
  </g>
  <g class="label-text" fill="var(--camomile-line)">
    <text class="brand-name" x="377" y="232" text-anchor="middle">VARNEO</text>
    <text class="tagline" x="377" y="264" text-anchor="middle">Natural Handmade Soap</text>
    <text class="variant-name" x="377" y="366" text-anchor="middle">camomile</text>
    <text class="variant-benefit" x="377" y="408" text-anchor="middle">Balance &amp; Mild</text>
  </g>
</svg>

</body>
</html>
```